Making 6 Posters and 2 large posters for coffee shop

We are Brindle Mug Depot (similar to a brewhollow), planning to make 3 boards for menu, 3 photos to be printed onto the board, and 2 large posters. (dimensions provided). We believe this is a very simple project with not much additional work required as all pictures have been provided.
We are asking for minimalist design. Very simple. All photos have been provided. 3 of the boards, and 2 for the large posters. The menu has been done but it is in PDF and require recreation (pls make similar design)
The menu board and the 3 other photos are roughly square shape. While dimensions are not provided by our contractors yet, designers can roughly get the dimension from the photos of the boards we are planning to replace.
All these posters will be printed with no frames. So it will look something like those menu board at brewhollow.
Urgently need it in next 24 hours.
Instructions all in PPT attached.
File Link provided:
http://qlinkbox.example/7hT3kWz
Thanks.
---- Edited
For the pictures, we are looking for borders like this if possible (VORN - expensive looking border but platinum white, and dark background.) for the large poster, we liek black themed background with some glow if possible around the cups like the kelvaro logo)
http://www.plumtemplates.example/images/thumbs/Onyx-Slate-psd48213.png
http://www.wirefable-news.example/wp-content/uploads/2013/11/kelvaro-signage.jpg
Target Market(s)
Professionals - Lawyers, Bankers, Brokers
Industry/Entity Type
Coffee Shop

```html
<!DOCTYPE html>
<html lang="en">
<head>
<meta charset="utf-8">
<title>Brindle Mug Depot — Banner</title>
<link rel="stylesheet" href="https://fonts.googleapis.com/css2?family=Jost:wght@600&display=swap">
<style>
  :root {
    --board-black: #0a0a0a;
    --board-grain: #151515;
    --frame-line: #b9b9b9;
    --title-grey: #a6a6a6;
    --cup-yellow: #f3d12a;
    --cup-yellow-deep: #d2ad08;
    --cup-glow: rgba(243, 209, 42, 0.28);
  }
  html, body {
    margin: 0;
    padding: 0;
    width: 1200px;
    height: 423px;
    overflow: hidden;
    background: var(--board-black);
  }
  .banner {
    position: relative;
    width: 1200px;
    height: 423px;
    background: radial-gradient(ellipse at 60% 45%, var(--board-grain) 0%, var(--board-black) 75%);
    overflow: hidden;
  }
  .banner__frame {
    position: absolute;
    inset: 0;
    width: 1200px;
    height: 423px;
  }
  .banner__cup {
    position: absolute;
    left: 57px;
    top: 118px;
    width: 354px;
    height: 194px;
    border-radius: 28px;
    background: radial-gradient(ellipse at 45% 40%, var(--cup-yellow) 0%, var(--cup-yellow-deep) 100%);
    box-shadow: 0 0 36px 6px var(--cup-glow);
  }
  .banner__title {
    position: absolute;
    left: 440px;
    top: 180px;
    width: 690px;
    margin: 0;
    font-family: "Jost", "Futura", sans-serif;
    font-weight: 600;
    font-size: 63px;
    line-height: 74px;
    letter-spacing: 2px;
    text-align: center;
    text-transform: uppercase;
    white-space: nowrap;
    color: var(--title-grey);
  }
</style>
</head>
<body>
  <main class="banner">
    <svg class="banner__frame" viewBox="0 0 1200 423" aria-hidden="true">
      <g fill="none" stroke="var(--frame-line)" stroke-width="1.5">
        <path d="M38 14 H1162 A24 24 0 0 0 1186 38 V385 A24 24 0 0 0 1162 409 H38 A24 24 0 0 0 14 385 V38 A24 24 0 0 0 38 14 Z"/>
        <path d="M40 22 H1160 A18 18 0 0 0 1178 40 V383 A18 18 0 0 0 1160 401 H40 A18 18 0 0 0 22 383 V40 A18 18 0 0 0 40 22 Z"/>
      </g>
    </svg>

    <div class="banner__cup" role="img" aria-label="Photo of a glossy yellow espresso cup on a matching saucer"></div>

    <h1 class="banner__title">Brindle Mug Depot</h1>
  </main>
</body>
</html>
```